Oil and Gas Industry training School Needs a Web Design

We need a web design for a new company based in Northern British Columbia Canada called "SKILLSPAN Industry Training Inc." Is a training facility that specializes in different aspects of Pipeline Construction training. We also offer compliance courses for Oil and Gas Industry. We would like to see designs that us the colours in our logo.

Target Market(s)

Is Men and women between 18-60 that want to work in the oil and gas industry

Industry/Entity Type

School

Number of Pages Required

5+ page

Font styles to use
Sans Serif

Colors
f37022
000000
333333
ffffff
848484
7f7f7f
c8c8c8
f68d4d
fee3d4

Requirements
Must have
• a easy back end for editing content! and adding additional pages if necessary.

```html
<!DOCTYPE html>
<html lang="en">
<head>
<meta charset="utf-8">
<title>SKILLSPAN Industry Training Inc.</title>
<link rel="stylesheet" href="https://fonts.googleapis.com/css2?family=Roboto:wght@400;500;700&family=Roboto+Condensed:wght@400;700&family=Open+Sans:wght@400;600;700&display=swap">
<style>
:root{
  --orange:#f37022;
  --orange-light:#f68d4d;
  --orange-pale:#fee3d4;
  --black:#000000;
  --ink:#333333;
  --grey:#848484;
  --grey-mid:#7f7f7f;
  --grey-light:#c8c8c8;
  --white:#ffffff;
  --topbar:#4a4a4a;
  --footer:#2b2b2b;
  --footer-base:#555555;
}
*{box-sizing:border-box;margin:0;padding:0}
html,body{width:849px;height:1200px;overflow:hidden;background:var(--white)}
body{position:relative;font-family:"Open Sans",Arial,sans-serif;color:var(--ink)}
.abs{position:absolute}

/* top bar */
.topbar{left:483px;top:0;width:366px;height:29px;background:var(--topbar);display:flex;align-items:center;gap:14px;padding-left:8px;color:var(--white);font-size:12px}
.topbar .item{display:flex;align-items:center;gap:8px}
.topbar .phone{font-family:"Roboto",sans-serif;font-size:14px;letter-spacing:.5px}
.topbar .dot{width:16px;height:16px;border-radius:50%;background:#6a6a6a}

/* header */
.brand{left:0;top:29px;width:356px;height:60px;background:var(--white);display:flex;align-items:center;padding-left:100px;gap:10px}
.brand-mark{width:40px;height:40px;border-radius:50%;background:var(--ink)}
.brand-name{font-family:"Roboto",sans-serif;font-weight:700;font-size:22px;color:var(--ink);line-height:1}
.brand-sub{font-family:"Roboto",sans-serif;font-size:9px;color:var(--ink);letter-spacing:1px;margin-top:3px}
.nav{left:356px;top:29px;width:493px;height:60px;background:var(--orange);display:flex;padding-left:11px}
.nav a{width:74px;height:60px;display:flex;flex-direction:column;align-items:center;justify-content:center;gap:5px;color:var(--white);text-decoration:none;font-family:"Roboto",sans-serif;font-size:11px;font-weight:500}
.nav a.active{background:#2e2e2e;width:60px;margin-right:8px}
.nav svg{width:14px;height:14px}

/* hero */
.hero{left:0;top:89px;width:849px;height:320px;background:linear-gradient(160deg,#6f7377 0%,#9aa0a4 40%,#c6cacc 70%,#8b8f92 100%)}
.hero-curve{left:0;top:340px;width:849px;height:80px}
.hero-copy{left:367px;top:163px;width:389px;height:120px;background:var(--orange);padding:12px 14px;font-family:"Roboto Condensed",sans-serif;color:var(--white);font-size:23px;line-height:30px}
.hero-copy .tag{background:var(--white);color:var(--ink);font-weight:700;padding:0 4px}
.dots{left:399px;top:346px;display:flex;gap:3px}
.dots span{width:10px;height:10px;border-radius:50%;background:var(--grey-light);border:2px solid var(--white)}
.dots span.on{background:var(--orange)}

/* welcome */
.welcome{left:93px;top:376px;width:663px;height:137px;background:var(--white);box-shadow:0 6px 10px rgba(0,0,0,.12);text-align:center;padding-top:12px}
.welcome h1{font-family:"Roboto",sans-serif;font-weight:400;font-size:22px;color:var(--orange);display:flex;align-items:center;justify-content:center;gap:8px}
.welcome h1 .mark{width:18px;height:18px;border-radius:50%;background:var(--ink)}
.welcome h1 b{color:var(--ink);font-weight:700;font-size:19px}
.welcome p{font-size:10px;line-height:16px;color:var(--ink);width:610px;margin:12px auto 8px}
.btn{display:inline-block;border:1px solid var(--orange);border-radius:14px;padding:4px 10px;font-size:9.5px;font-weight:600;color:var(--ink);background:var(--white);text-transform:uppercase;font-family:"Open Sans",sans-serif}

/* training */
.training{left:0;top:524px;width:849px;height:280px;background:var(--orange);color:var(--white);text-align:center}
.training h2{font-family:"Roboto",sans-serif;font-weight:400;font-size:23px;margin-top:13px}
.training .rule{width:130px;height:1px;background:var(--orange-light);margin:9px auto 0}
.course{position:absolute;top:64px;width:210px;text-align:center}
.course svg{width:84px;height:84px}
.course h3{font-family:"Roboto",sans-serif;font-weight:400;font-size:15px;margin-top:10px}
.course p{font-size:10px;line-height:13px;margin:6px 0 14px}
.course .btn{background:transparent;color:var(--white);border-color:var(--orange-pale)}

/* info columns */
.col{top:804px;padding-top:18px}
.col h4{font-family:"Roboto",sans-serif;font-weight:400;font-size:15px;color:var(--ink);border-bottom:1px solid var(--grey-light);padding-bottom:3px}
.col h4 span{color:var(--orange)}
.reviews{left:100px;width:207px}
.avatar{position:absolute;left:2px;top:52px;width:60px;height:60px;border-radius:50%;background:linear-gradient(160deg,#e9d7c4,#c9a98a);border:3px solid var(--white);box-shadow:0 0 0 1px var(--grey-light)}
.student{position:absolute;left:68px;top:66px;font-size:10px;color:var(--orange);font-weight:700;line-height:15px}
.student small{display:block;font-weight:600;font-size:10px}
.quote{position:absolute;left:0;top:122px;font-size:10px;line-height:15px;color:var(--grey)}
.reviews .btn,.news .btn{position:absolute;top:202px;left:0;text-transform:none}
.contact{left:325px;width:203px}
.field{width:203px;height:24px;border:1px solid var(--grey-light);margin-top:6px;font-size:9px;padding:5px 7px;color:var(--grey)}
.field.first{margin-top:15px}
.field.area{height:52px}
.contact .btn{margin-top:12px}
.news{left:551px;width:206px}
.story{position:relative;padding-left:20px;margin-top:14px;font-size:10px;line-height:13px}
.story+.story{border-top:1px solid var(--grey-light);padding-top:10px;margin-top:10px}
.story .cal{position:absolute;left:0;top:1px;width:13px;height:12px;border:1.5px solid var(--grey-mid);border-top-width:3px}
.story+.story .cal{top:11px}
.story .date{color:var(--orange);font-weight:700;font-size:11px}
.story b{color:var(--ink);display:block}
.story span{color:var(--ink)}
.divider{top:830px;width:1px;height:190px;background:#e4e4e4}

/* footer */
.footer{left:0;top:1049px;width:849px;height:124px;background:var(--footer);color:var(--white)}
.footer::before{content:"";position:absolute;left:0;top:0;width:849px;height:2px;background:var(--orange)}
.fcol{position:absolute;top:18px}
.fcol h5{font-family:"Roboto",sans-serif;font-weight:400;font-size:14px;padding-bottom:5px;border-bottom:1px solid #444;margin-bottom:10px}
.links{display:grid;grid-template-columns:77px 77px;row-gap:9px;font-size:10px;color:var(--grey-light)}
.links span::before{content:"→";margin-right:6px;font-size:8px}
.fline{display:flex;gap:8px;font-size:10px;line-height:13px;color:var(--grey-light);margin-bottom:6px}
.fline .ic{width:10px;flex:none;color:var(--white)}
.fline.big{font-family:"Roboto",sans-serif;font-size:13px;color:var(--white)}
.social{display:grid;grid-template-columns:86px 86px;row-gap:9px;font-size:10px}
.social span{display:flex;align-items:center;gap:6px}
.social i{width:18px;height:18px;border-radius:50%;background:var(--white)}
.fmark{left:670px;top:1065px;width:56px;height:56px;border-radius:50%;background:#555}
.copyright{left:0;top:1173px;width:849px;height:27px;background:var(--footer-base);color:var(--white);font-size:10px;text-align:center;line-height:27px}
</style>
</head>
<body>

<div class="abs topbar">
  <div class="item"><span class="dot"></span><span class="phone">555 - 014 - 2290</span></div>
  <div class="item"><span class="dot"></span><span>info@skillspan-training.ca</span></div>
</div>

<header>
  <div class="abs brand">
    <span class="brand-mark"></span>
    <div>
      <div class="brand-name">SKILLSPAN</div>
      <div class="brand-sub">INDUSTRY TRAINING INC.</div>
    </div>
  </div>
  <nav class="abs nav">
    <a class="active" href="#"><svg viewBox="0 0 14 14"><circle cx="7" cy="7" r="5" fill="none" stroke="#fff" stroke-width="2.5" stroke-dasharray="2 1.6"/><circle cx="7" cy="7" r="2" fill="#fff"/></svg>ABOUT</a>
    <a href="#"><svg viewBox="0 0 14 14"><rect x="2" y="2" width="9" height="10" fill="none" stroke="#fff" stroke-width="1.4"/><path d="M6 9l6-6" stroke="#fff" stroke-width="1.6"/></svg>COURSES</a>
    <a href="#"><svg viewBox="0 0 14 14"><path d="M2 2l10 10M12 2L2 12" stroke="#fff" stroke-width="2"/></svg>SERVICES</a>
    <a href="#"><svg viewBox="0 0 14 14"><rect x="1" y="2" width="12" height="8" fill="none" stroke="#fff" stroke-width="1.4"/><path d="M5 10v3M9 10v3" stroke="#fff" stroke-width="1.4"/></svg>TRAINING</a>
    <a href="#"><svg viewBox="0 0 14 14"><path d="M1 2h12v8H5l-3 3v-3H1z" fill="none" stroke="#fff" stroke-width="1.4"/></svg>NEWS</a>
    <a href="#"><svg viewBox="0 0 14 14"><path d="M3 1l3 3-2 2c1 2 2 3 4 4l2-2 3 3-2 2C6 13 1 8 1 3z" fill="#fff"/></svg>CONTACT</a>
  </nav>
</header>

<section>
  <div class="abs hero" role="img" aria-label="Photo of two pipeline workers in hard hats and safety glasses inside an industrial plant"></div>
  <svg class="abs hero-curve" viewBox="0 0 849 80" preserveAspectRatio="none"><path d="M0 0 Q424 70 849 0 V80 H0 Z" fill="#ffffff"/></svg>
  <div class="abs hero-copy"><span class="tag">SKILLSPAN</span> Is a training facility that Specializes In Different Aspects Of Pipeline Construction Training.</div>
  <div class="abs dots"><span class="on"></span><span></span><span></span><span></span></div>

  <div class="abs welcome">
    <h1><span class="mark"></span>Welcome to <b>SKILLSPAN</b></h1>
    <p>Lorem Ipsum is simply dummy text of the printing and typesetting industry. Lorem Ipsum has been the industry's standard dummy text ever since the 1500s, when an unknown printer took a galley of type and scrambled it to make a type specimen book. It has survived not only five centuries, but also the leap into electronic typesetting, remaining essentially unchanged.</p>
    <span class="btn">Read More</span>
  </div>
</section>

<section class="abs training">
  <h2>Our Training</h2>
  <div class="rule"></div>
  <div class="course" style="left:98px">
    <svg viewBox="0 0 84 84"><circle cx="42" cy="42" r="38" fill="#333"/><circle cx="42" cy="42" r="26" fill="none" stroke="#f37022" stroke-width="3"/><rect x="31" y="32" width="22" height="18" fill="none" stroke="#fff" stroke-width="2.5"/><path d="M42 32v18" stroke="#fff" stroke-width="2"/></svg>
    <h3>TRAINING ONE</h3>
    <p>Lorem Ipsum is simply dummy text o printing and typesetting .Lorem Ipsum has simply dummy text o printing.</p>
    <span class="btn">Read More</span>
  </div>
  <div class="course" style="left:323px">
    <svg viewBox="0 0 84 84"><circle cx="42" cy="42" r="38" fill="#333"/><circle cx="42" cy="42" r="26" fill="none" stroke="#f37022" stroke-width="3"/><rect x="29" y="30" width="26" height="19" fill="none" stroke="#fff" stroke-width="2.5"/><path d="M34 45l5-5 4 3 6-7M42 49v6" stroke="#fff" stroke-width="2" fill="none"/></svg>
    <h3>TRAINING TWO</h3>
    <p>Lorem Ipsum is simply dummy text o printing and typesetting .Lorem Ipsum has simply dummy text o printing.</p>
    <span class="btn">Read More</span>
  </div>
  <div class="course" style="left:548px">
    <svg viewBox="0 0 84 84"><circle cx="42" cy="42" r="38" fill="#333"/><circle cx="42" cy="42" r="26" fill="none" stroke="#f37022" stroke-width="3"/><rect x="31" y="30" width="18" height="23" fill="none" stroke="#fff" stroke-width="2.5"/><path d="M40 49l12-12 3 3-12 12h-3z" fill="#fff"/></svg>
    <h3>TRAINING THREE</h3>
    <p>Lorem Ipsum is simply dummy text o printing and typesetting .Lorem Ipsum has simply dummy text o printing.</p>
    <span class="btn">Read More</span>
  </div>
</section>

<section>
  <div class="abs col reviews">
    <h4><span>Students</span> Review</h4>
    <div class="avatar" role="img" aria-label="Portrait photo of a student"></div>
    <div class="student">STUDENT NAME<small>Qualification, City</small></div>
    <p class="quote"><span style="color:#c8c8c8;font-size:16px">“</span> Lorem ipsum dolor sit amet, adipiscing elit, sed di nonummy nibh euismod ti laoreet dolore magna alnquam erat volutpat. Ut wisi enim ad minim veniam euismod tinci laoreet dolore magna...</p>
    <span class="btn">Read More</span>
  </div>
  <div class="abs divider" style="left:314px"></div>
  <div class="abs col contact">
    <h4><span>Contact</span> Us</h4>
    <div class="field first">Name</div>
    <div class="field">Phone</div>
    <div class="field">Email</div>
    <div class="field area">Message</div>
    <span class="btn">Submit</span>
  </div>
  <div class="abs divider" style="left:539px"></div>
  <div class="abs col news">
    <h4><span>Latest</span> News</h4>
    <div class="story"><i class="cal"></i><div class="date">25Sept, 2014</div><b>Lorem ipsum dolor sit amet</b><span>Lorem Ipsum is simply dummy printing and typesetting industry.</span></div>
    <div class="story"><i class="cal"></i><div class="date">25Sept, 2014</div><b>Lorem ipsum dolor sit amet</b><span>nibh euismod ti laoreet dolore alnquam erat volutpat. Ut wisi enim ad mi veniam laoreet dolore alnquam.</span></div>
    <span class="btn">Read More</span>
  </div>
</section>

<footer class="abs footer">
  <div class="fcol" style="left:94px;width:150px">
    <h5>Quick Links</h5>
    <div class="links"><span>About</span><span>Training</span><span>Courses</span><span>News</span><span>Services</span><span>Contact Us</span></div>
  </div>
  <div class="fcol" style="left:279px;width:150px">
    <h5>Contact Us</h5>
    <div class="fline"><span class="ic">●</span><span>Duis autem vel eum iriu dolor sed di nonummy euismod.</span></div>
    <div class="fline big"><span class="ic">✆</span><span>555 - 014 - 2290</span></div>
    <div class="fline"><span class="ic">✉</span><span>info@skillspan-training.ca</span></div>
  </div>
  <div class="fcol" style="left:465px;width:170px">
    <h5>Follow Us</h5>
    <div class="social"><span><i></i>Facepage</span><span><i></i>Chirper</span><span><i></i>Circles Plus</span><span><i></i>Linkwork</span></div>
  </div>
</footer>
<div class="abs fmark"></div>
<div class="abs copyright">Copyright © 2014 Skillspan</div>

</body>
</html>
```